Cleaning Service Company In need of Good Web presence.

The company is a cleaning service company which provides professional staff and service for cleaning. This is a project to build a site that is both solid and a strong recognition of our organization. It is supposed to show quality, cleanliness, professionalism. The use of images and art for imagery is all good just to have a site that is consistent and solid. There might be a chance to make stationary, logo and business cars if someone feels they can build a brand that is consistent. The image we are going for is clean solid and to stand out. Finally stationary should not be expensive to print.

Current logo is attached and can be used or can be made more creative.

Target Market(s)

Corporate and Government entities, that will feel that this company has a brand that sets it apart from the rest. The company is new so the modification of the logo will not be an issue if a more solid brand come out of this project. The idea is to have a clean consistent product that stands our from others in terms of website, stationary, etc

Industry/Entity Type

Cleaning Service

Contact Information for Business Card

P.O.Box 41967
Riffa
Kingdom of Bahrain

Logo Text

Maple Ridge Solutions

Number of Pages Required

4 page

Font styles to use
Sans Serif

Colors
abd036
cadf82
eaf2ce
9bcb3b

Requirements
Must have
• Green Color to be used in order to stick to the name. Also the creativity and boldness in an elegant manner.
Nice to have
• Arabic name of company
• نوفا بلو للحلول ذ.م.م
• if cannot be put at least make a location should be chosen
• Also could be a bit of 3D given to the logo if it could stay elegent.
Should not have
• Should not show people cleaning.

```html
<!DOCTYPE html>
<html lang="en">
<head>
<meta charset="utf-8">
<title>Maple Ridge Solutions — Professional Cleaning</title>
<link href="https://fonts.googleapis.com/css2?family=Righteous&family=Roboto:wght@400;500;700&display=swap" rel="stylesheet">
<style>
:root{
  --green:#9bcb3b;
  --green-mid:#abd036;
  --green-soft:#cadf82;
  --green-pale:#eaf2ce;
  --ink:#222222;
  --muted:#6f6f6f;
  --white:#ffffff;
  --line:#dcdcdc;
}
*{box-sizing:border-box;margin:0;padding:0}
html,body{width:1200px;height:3732px;overflow:hidden}
body{font-family:"Roboto",Arial,sans-serif;color:var(--ink);background:var(--white);position:relative}
.display{font-family:"Righteous","Trebuchet MS",sans-serif;font-weight:400}
.btn{display:inline-block;background:var(--green);color:var(--white);font-size:15px;font-weight:500;padding:12px 26px;border-radius:3px;white-space:nowrap}
.abs{position:absolute}

/* top bar + nav */
.topbar{top:0;left:0;width:1200px;height:20px;background:var(--green);color:var(--white);font-size:11px;display:flex;align-items:center;gap:20px;padding-left:116px}
.nav{top:20px;left:0;width:1200px;height:60px;background:var(--white);display:flex;align-items:center;justify-content:center;gap:30px;font-size:13px;padding-left:60px}
.nav a{color:var(--ink);text-decoration:none}
.nav a.active{color:var(--green)}
.nav .brand{display:flex;align-items:center;gap:8px;font-size:11px;font-weight:700;color:var(--green)}
.nav .brand i{width:26px;height:26px;border-radius:50%;background:var(--green);display:block}

/* hero */
.hero{top:80px;left:0;width:1200px;height:440px;overflow:hidden;
  background:
    radial-gradient(ellipse 260px 140px at 520px 330px,rgba(171,208,54,.55),rgba(171,208,54,0) 70%),
    radial-gradient(ellipse 200px 120px at 1000px 390px,rgba(80,120,60,.35),rgba(80,120,60,0) 70%),
    linear-gradient(112deg,rgba(0,0,0,0) 0 8%,rgba(202,223,130,.75) 8% 16%,rgba(0,0,0,0) 16% 100%),
    linear-gradient(112deg,rgba(0,0,0,0) 0 30%,rgba(202,223,130,.7) 30% 36%,rgba(0,0,0,0) 36% 100%),
    linear-gradient(90deg,rgba(0,0,0,0) 0 76%,rgba(171,208,54,.7) 76% 82%,rgba(0,0,0,0) 82% 100%),
    linear-gradient(180deg,#eef0ea 0%,#f8f9f5 55%,#e3e6dc 100%)}
.hero h1{position:absolute;top:152px;width:100%;text-align:center;font-size:42px;color:#1f1f1f}
.hero .btn{position:absolute;top:226px;left:533px}
.dots{position:absolute;top:400px;left:588px;display:flex;gap:8px}
.dots span{width:8px;height:8px;border-radius:50%;background:#fff;opacity:.9}

/* services */
.services{top:520px;left:0;width:1200px;height:460px;background:var(--white)}
.services .art{position:absolute;left:160px;top:60px;width:360px;height:340px;
  background:
    radial-gradient(ellipse 70px 150px at 190px 170px,rgba(47,190,190,.75),rgba(47,190,190,0) 70%),
    radial-gradient(circle 60px at 110px 240px,rgba(90,90,110,.45),rgba(90,90,110,0) 70%),
    radial-gradient(circle 50px at 270px 280px,rgba(155,203,59,.5),rgba(155,203,59,0) 70%),
    radial-gradient(ellipse 180px 160px at 180px 170px,#dff2f5 0%,#eef8fa 60%,rgba(255,255,255,0) 100%)}
.services h2{position:absolute;left:628px;top:92px;font-size:30px;line-height:34px}
.services p{position:absolute;left:790px;top:214px;width:290px;font-size:12px;line-height:19px;color:var(--muted)}
.services .btn{position:absolute;left:786px;top:318px;font-size:14px;padding:11px 24px}

/* family band */
.family{top:980px;left:0;width:1200px;height:460px;
  background:
    radial-gradient(ellipse 260px 60px at 300px 400px,rgba(150,140,130,.45),rgba(150,140,130,0) 70%),
    radial-gradient(ellipse 90px 140px at 1080px 300px,rgba(171,208,54,.35),rgba(171,208,54,0) 70%),
    radial-gradient(ellipse 300px 200px at 900px 150px,rgba(255,255,255,.8),rgba(255,255,255,0) 70%),
    linear-gradient(90deg,#dcd8d2 0%,#ebe8e4 30%,#f3f2f0 60%,#e4e3dd 100%)}
.family h2{position:absolute;top:136px;width:100%;text-align:center;font-size:40px;line-height:44px;color:#1f1f1f}
.family p{position:absolute;top:236px;width:100%;text-align:center;font-size:12px;color:#333}
.family .btn{position:absolute;top:290px;left:528px;font-size:14px;padding:11px 24px}

/* how we do it */
.how{top:1440px;left:0;width:1200px;height:500px;background:var(--green-pale)}
.how h2{position:absolute;top:70px;width:100%;text-align:center;font-size:28px}
.how .sub{position:absolute;top:112px;width:100%;text-align:center;font-size:10px;color:var(--muted)}
.how .photo{position:absolute;left:120px;top:180px;width:440px;height:220px;
  background:
    radial-gradient(ellipse 90px 70px at 110px 140px,rgba(45,100,70,.9),rgba(45,100,70,0) 75%),
    radial-gradient(ellipse 110px 90px at 80px 170px,rgba(200,150,120,.6),rgba(200,150,120,0) 75%),
    linear-gradient(90deg,#c9d2c6 0%,#eceeea 45%,#f9f9f7 100%)}
.faq{position:absolute;left:632px;width:440px;background:var(--white);border:1px solid var(--line)}
.faq h3{font-size:12px;font-weight:500;padding:12px 16px}
.faq p{font-size:10px;line-height:16px;color:var(--muted);padding:0 16px 12px}
.faq.open{top:180px;height:104px}
.faq.closed{top:300px;height:46px;display:flex;justify-content:space-between;align-items:center;padding-right:16px}
.faq.closed h3{padding:0 16px}

/* testimonial */
.testimonial{top:1940px;left:0;width:1200px;height:340px;
  background:
    radial-gradient(ellipse 160px 90px at 260px 290px,rgba(70,110,170,.55),rgba(70,110,170,0) 75%),
    radial-gradient(ellipse 200px 110px at 880px 270px,rgba(90,90,100,.45),rgba(90,90,100,0) 75%),
    radial-gradient(ellipse 120px 70px at 1100px 200px,rgba(155,203,59,.5),rgba(155,203,59,0) 75%),
    linear-gradient(90deg,#6e6f73 0%,#a7a6a4 35%,#d9d6d0 65%,#c3beb5 100%)}
.testimonial .mark{position:absolute;left:589px;top:52px;width:22px;height:22px;border-radius:50%;background:var(--green)}
.testimonial blockquote{position:absolute;left:152px;top:96px;width:820px;font-size:24px;line-height:28px;color:var(--white)}
.testimonial .who{position:absolute;left:152px;top:186px;font-size:12px;color:var(--white);font-weight:700}
.testimonial .role{position:absolute;left:152px;top:204px;font-size:10px;color:#eeeeee}

/* contact form */
.contact{top:2280px;left:0;width:1200px;height:480px;background:var(--green-pale)}
.field{position:absolute;background:var(--white);border:1px solid var(--line);font-size:11px;color:var(--muted);padding:11px 14px}
.captcha{position:absolute;left:884px;top:288px;font-size:11px;color:var(--muted);display:flex;align-items:center;gap:8px}
.captcha span{width:52px;height:36px;background:var(--white);border:1px solid var(--line);display:block}
.contact .btn{position:absolute;left:980px;top:288px;padding:10px 20px;font-size:13px}

/* blog */
.blog{top:2760px;left:0;width:1200px;height:610px;background:var(--green-pale)}
.blog h2{position:absolute;top:0;width:100%;text-align:center;font-size:28px;color:var(--green)}
.blog .sub{position:absolute;top:44px;width:100%;text-align:center;font-size:11px;color:var(--muted)}
.blog .post{position:absolute;top:192px;width:508px;height:336px}
.post.one{left:64px;
  background:
    radial-gradient(ellipse 110px 90px at 140px 200px,rgba(45,100,70,.95),rgba(45,100,70,0) 75%),
    radial-gradient(ellipse 150px 120px at 90px 250px,rgba(205,150,120,.65),rgba(205,150,120,0) 75%),
    linear-gradient(90deg,#cdd5ca 0%,#ecefea 45%,#f9f9f7 100%)}
.post.two{left:628px;
  background:
    radial-gradient(ellipse 200px 90px at 260px 40px,rgba(60,60,60,.65),rgba(60,60,60,0) 75%),
    radial-gradient(ellipse 160px 220px at 420px 180px,rgba(255,255,255,.95),rgba(255,255,255,0) 75%),
    linear-gradient(180deg,#bdbdbd 0%,#e8e8e8 30%,#f2f2f2 60%,#8f8f8f 100%)}

/* footer */
.footer{top:3370px;left:0;width:1200px;height:310px;background:var(--white);border-top:1px solid var(--line)}
.footer .seal{position:absolute;left:140px;top:60px;width:200px;height:200px;border-radius:50%;background:var(--green);display:flex;align-items:center;justify-content:center;text-align:center;color:var(--white);font-size:18px;font-weight:700;line-height:23px;padding:24px}
.footer .col{position:absolute;top:62px;width:200px}
.footer h4{font-size:16px;color:var(--green);margin-bottom:8px;font-weight:700;line-height:18px}
.footer .col p,.footer li{font-size:10px;line-height:16px;color:var(--muted);list-style:none}
.footer li::before{content:"›";color:var(--green);margin-right:6px}
.footer .contact-col h4{color:var(--ink)}
.bottombar{top:3680px;left:0;width:1200px;height:52px;background:var(--green);color:var(--white);font-size:11px;display:flex;align-items:center;justify-content:space-between;padding:0 100px 0 24px}
.socials{display:flex;gap:16px}
.socials span{width:14px;height:14px;border-radius:50%;background:var(--white);display:block}
</style>
</head>
<body>

<div class="abs topbar"><span>+973 1700 4455</span><span>hello@mapleridge.bh</span></div>

<nav class="abs nav">
  <a class="active" href="#">Home</a>
  <a href="#">Features</a>
  <span class="brand"><i></i></span>
  <a href="#">About Us</a>
  <a href="#">Blog</a>
</nav>

<section class="abs hero" role="img" aria-label="Bright clean living room with green sofa, green curtains and sunlit windows">
  <h1 class="display">Lets us do your dirty work .</h1>
  <span class="btn">Booking now</span>
  <div class="dots"><span></span><span></span></div>
</section>

<section class="abs services">
  <div class="art" role="img" aria-label="Illustration of professional cleaning equipment: vacuum, bucket and mop"></div>
  <h2 class="display">Professional Cleaning<br>Services</h2>
  <p>Regular vacuuming and stain removal protects your floors, but deep cleaning needs the trained hands of professional staff. We keep every room fresh and safe.</p>
  <span class="btn">Booking now!</span>
</section>

<section class="abs family" role="img" aria-label="Clean white living room interior with plants">
  <h2 class="display">Keep your home clean and<br>tiedy for you and your family.</h2>
  <p>You deserve a clean and tidy house. It will keep you safe and protected from illness and treat safe for your family</p>
  <span class="btn">Booking now</span>
</section>

<section class="abs how">
  <h2 class="display">How we do it ?</h2>
  <p class="sub">We are doing it in these 3 steps</p>
  <div class="photo" role="img" aria-label="Green sponge wiping a white surface"></div>
  <div class="faq open">
    <h3>What is method of cleaning ?</h3>
    <p>Our trained crews use eco-friendly products, steam cleaning and fine microfiber cloths, a method proven to lift dirt while keeping surfaces safe and gleaming.</p>
  </div>
  <div class="faq closed">
    <h3>Do I need a vacuum before clean served ?</h3>
    <svg width="10" height="10" viewBox="0 0 10 10"><path d="M2 3l3 4 3-4" stroke="#6f6f6f" stroke-width="1.5" fill="none"/></svg>
  </div>
</section>

<section class="abs testimonial" role="img" aria-label="Family relaxing together in a tidy home">
  <span class="mark"></span>
  <blockquote class="display">"Great Company make my own Company clean and tidy, and they call me after one week and make follow up to make everything is good"</blockquote>
  <div class="who">Lena Harlow</div>
  <div class="role">CEO, Harlow Trading Company</div>
</section>

<section class="abs contact">
  <div class="field" style="left:120px;top:68px;width:460px;height:38px">Name</div>
  <div class="field" style="left:620px;top:68px;width:452px;height:38px">Email Address</div>
  <div class="field" style="left:120px;top:132px;width:952px;height:132px">Message</div>
  <div class="captcha">4 + 5 = <span></span></div>
  <span class="btn">Submit</span>
</section>

<section class="abs blog">
  <h2 class="display">Our Blog</h2>
  <p class="sub">Keep you updated with our latest news.</p>
  <div class="post one" role="img" aria-label="Blog photo: green sponge cleaning a surface"></div>
  <div class="post two" role="img" aria-label="Blog photo: bright modern white hallway"></div>
</section>

<footer class="abs footer">
  <div class="seal">Maple Ridge Solutions</div>
  <div class="col" style="left:370px">
    <h4>About Us</h4>
    <p>With over 10 years of experience in the cleaning industry our reputation has grown and grown. Find out what we can do for you.</p>
  </div>
  <div class="col" style="left:612px">
    <h4>Important links</h4>
    <ul><li>Home</li><li>Features</li><li>About Us</li><li>Blog</li></ul>
  </div>
  <div class="col contact-col" style="left:876px">
    <h4>Contact<br>information</h4>
    <p>P.O.Box 41967, Riffa,<br>Kingdom of Bahrain<br>Phone: +973 1700 4455</p>
  </div>
</footer>

<div class="abs bottombar"><span>Powered by Maple Ridge Solutions</span><div class="socials"><span></span><span></span><span></span></div></div>

</body>
</html>
```